icon button design for a mid to high end travel concierge app

Design an icon with an appropriate catchy and memorable name for an online travel concierge app targeting discerning Asian travellers. The app will allow uses to chat with our AI chat bot to organise special events tickets, restaurant reservations, destination recommendations, organising baby sitters and etc. The app is designed to minimize the hassle in travel planning and logistics. We seek a clean and elegant but memorable icon design for the discerning Asian travellers primarily targeting Chinese, Koreans and Japanese. Ideally the design works across different cultural boundaries.

Our company is a startup and don’t have a company logo yet. The app is independent of the company. We like to keep the icon button and name of app open to interpretation by the designers and would like some imagination in the app name other than just Travel Concierge given our design brief.

Target Market(s)

Mid to Upper income bracket, Asian travellers from China, Korea and Japan.

Industry/Entity Type

Travel Industry

Font styles to use
Serif
Sans Serif

Colors

Designer to choose colors to be used in the design.

Requirements
Must have
• Icon, a suggested name for the app conveying the message of an intelligent travel concierge at your finger tip for the discerning travelers from Asia exploring the world.
Nice to have
• We have contemplated a few names but they have too many syllables. Maximum 3 syllables for the app’s names. Such as Movana (not what we seek).

```html
<!DOCTYPE html>
<html lang="en">
<head>
<meta charset="utf-8">
<title>Movana – Sign in</title>
<link rel="stylesheet" href="https://fonts.googleapis.com/css2?family=Montserrat:wght@300;400;600;700&display=swap">
<style>
  :root {
    --navy-top: #2c3847;
    --navy-mid: #1d2633;
    --navy-bottom: #0c141f;
    --band: #ffffff;
    --text: #ffffff;
    --text-soft: #d7dce2;
    --rule: #9aa3ad;
    --accent: #d40f42;
  }
  * { box-sizing: border-box; margin: 0; padding: 0; }
  html, body { width: 858px; height: 1200px; overflow: hidden; }
  body { font-family: "Montserrat", sans-serif; color: var(--text); }
  .screen {
    position: relative;
    width: 858px;
    height: 1200px;
    overflow: hidden;
    background: linear-gradient(180deg, var(--navy-top) 0%, var(--navy-mid) 50%, var(--navy-bottom) 100%);
  }
  .bands { position: absolute; inset: 0; }
  .brand {
    position: absolute; left: 108px; top: 158px;
    display: flex; align-items: center; gap: 34px;
  }
  .brand-mark {
    width: 88px; height: 88px; border-radius: 50%;
    border: 4px solid var(--text);
  }
  .brand-name { font-size: 56px; font-weight: 400; letter-spacing: 2px; line-height: 1; }
  .headline {
    position: absolute; left: 106px; top: 290px;
    font-size: 42px; font-weight: 600; line-height: 54px;
  }
  .tagline {
    position: absolute; left: 106px; top: 420px;
    font-size: 35px; font-weight: 300; line-height: 46px; color: var(--text-soft);
  }
  .field {
    position: absolute; left: 96px; width: 666px;
    border-bottom: 2px solid var(--rule);
    font-size: 40px; font-weight: 300; color: var(--text-soft);
    padding-bottom: 10px; letter-spacing: 1px;
  }
  .field-email { top: 566px; }
  .field-password { top: 674px; }
  .submit {
    position: absolute; left: 566px; top: 800px;
    width: 200px; height: 200px; border-radius: 50%;
    background: var(--accent);
    display: flex; align-items: center; justify-content: center;
  }
  .signup {
    position: absolute; left: 108px; top: 1085px;
    font-size: 34px; line-height: 44px; font-weight: 300; color: var(--text-soft);
  }
  .signup-link { display: block; color: var(--accent); font-weight: 700; }
</style>
</head>
<body>
<main class="screen">
  <svg class="bands" width="858" height="1200" viewBox="0 0 858 1200" aria-hidden="true">
    <defs>
      <linearGradient id="band-fade" x1="858" y1="730" x2="152" y2="1200" gradientUnits="userSpaceOnUse">
        <stop offset="0" stop-color="#ffffff" stop-opacity="0"/>
        <stop offset="0.12" stop-color="#ffffff" stop-opacity="0.12"/>
        <stop offset="0.45" stop-color="#ffffff" stop-opacity="0.03"/>
        <stop offset="0.7" stop-color="#ffffff" stop-opacity="0.1"/>
        <stop offset="1" stop-color="#ffffff" stop-opacity="0.12"/>
      </linearGradient>
    </defs>
    <line x1="-40" y1="555" x2="900" y2="1045" stroke="var(--band)" stroke-opacity="0.1" stroke-width="90"/>
    <line x1="900" y1="700" x2="150" y2="1240" stroke="url(#band-fade)" stroke-width="100"/>
  </svg>

  <header class="brand">
    <span class="brand-mark" role="img" aria-label="App icon"></span>
    <span class="brand-name">Movana</span>
  </header>

  <h1 class="headline">Your online travel planner<br>and concierge</h1>
  <p class="tagline">Let us plan your vacation<br>for you</p>

  <div class="field field-email">Email</div>
  <div class="field field-password">Password</div>

  <div class="submit" role="button" aria-label="Sign in">
    <svg width="110" height="80" viewBox="0 0 110 80" aria-hidden="true">
      <path d="M8 40 H100 M66 6 L100 40 L66 74" fill="none" stroke="#ffffff" stroke-width="5" stroke-linecap="round" stroke-linejoin="round"/>
    </svg>
  </div>

  <p class="signup">Don’t have an account?<span class="signup-link">Register</span></p>
</main>
</body>
</html>
```